SUMMIT GATHERING 2021. August 20th -22nd.

The Hosts of the conference: Grace Tabernacle-Pastors Ron n Molly ( Picture with two persons)

Guest Minister: Bishop Lorna Kiprotich. (Cedar Ridge Evangelist)

Venue:
Seattle Harborgate Lodge. 4817 North 92nd Avenue Seattle, WA 98134.

Conference times.
Friday August 20th 6pm-8:30pm
Saturday August 21st. 6pm-8:30pm

Sunday August 22nd 10am-1pm
“ CHURCH RENEWAL SERVICE”

5pm-7:30pm
TWOFOLD BLESSING SERVICE.

Target Market(s)

18-55

Industry/Entity Type

Religious/ Entertainment.

Requirements
Must have
• A highlight of the Relaunch service on Sunday August 22nd 5pm-7:30pm.
Nice to have
• Excellent ideas….

```html
<!DOCTYPE html>
<html lang="en">
<head>
<meta charset="utf-8">
<title>Summit Gathering 2021</title>
<link rel="stylesheet" href="https://fonts.googleapis.com/css2?family=Montserrat:wght@200;400;500;700;800;900&display=swap">
<style>
  :root {
    --red: #e0120e;
    --red-deep: #c40f0c;
    --ink: #1e1e1e;
    --black: #0b0b0b;
    --paper: #ffffff;
    --dark-panel: #151515;
    --grey-text: #3a3a3a;
  }
  html, body { margin: 0; padding: 0; overflow: hidden; }
  body { width: 800px; height: 1200px; background: var(--paper); font-family: "Montserrat", sans-serif; }
  .poster { position: relative; width: 800px; height: 1200px; overflow: hidden; background: var(--paper); color: var(--ink); }

  .brand { position: absolute; left: 65px; top: 59px; width: 158px; height: 202px; display: flex; flex-direction: column; align-items: center; justify-content: center; gap: 14px; }
  .brand-mark { width: 44px; height: 44px; background: var(--ink); }
  .brand-name { font-weight: 700; font-size: 18px; color: var(--ink); text-align: center; line-height: 1.2; text-transform: uppercase; letter-spacing: 1px; }

  .title { position: absolute; left: 60px; top: 284px; margin: 0; line-height: 1; }
  .title-line-1 { display: block; font-weight: 900; font-size: 66px; letter-spacing: -3px; color: var(--ink); }
  .title-line-2 { display: block; font-weight: 800; font-size: 52px; letter-spacing: -2px; color: var(--red); margin-top: 6px; }
  .title-year { display: block; font-weight: 200; font-size: 104px; letter-spacing: -4px; color: var(--ink); margin-top: -2px; }

  .hosts-photo { position: absolute; left: 440px; top: 57px; width: 317px; height: 492px; background: var(--paper); box-shadow: 0 0 8px rgba(0,0,0,.18); }
  .hosts-photo-fill { position: absolute; left: 4px; top: 5px; right: 4px; bottom: 4px; background: linear-gradient(160deg, #5a2bd8 0%, #b02ac9 28%, #6d3a45 55%, #c9c3bd 100%); }

  .info-band { position: absolute; left: 0; top: 551px; width: 800px; height: 136px; background: linear-gradient(90deg, var(--red-deep), var(--red)); }
  .info-band svg { position: absolute; left: 0; top: 0; }
  .venue-heading { position: absolute; left: 60px; top: 16px; margin: 0; font-weight: 800; font-size: 19px; letter-spacing: -0.6px; color: var(--paper); }
  .venue-address { position: absolute; left: 60px; top: 68px; margin: 0; font-weight: 500; font-size: 16px; line-height: 23px; color: var(--paper); letter-spacing: .3px; }
  .band-divider { position: absolute; left: 429px; top: 32px; height: 88px; border-left: 1.5px dashed rgba(255,255,255,.85); }
  .hosts-label { position: absolute; left: 452px; top: 31px; margin: 0; font-weight: 400; font-size: 15px; letter-spacing: .8px; color: var(--paper); white-space: nowrap; }
  .hosts-names { position: absolute; left: 452px; top: 56px; margin: 0; font-weight: 800; font-size: 17px; line-height: 26px; letter-spacing: .5px; color: var(--paper); white-space: nowrap; }

  .schedule { position: absolute; left: 0; top: 700px; width: 800px; height: 407px; background: radial-gradient(ellipse at 55% 50%, #2b2b2b 0%, var(--dark-panel) 60%, var(--black) 100%); }
  .guest-photo { position: absolute; left: 0; top: 718px; width: 380px; height: 482px; background: linear-gradient(180deg, #2a1e18 0%, #6b4331 38%, #5d5d58 70%, #3d3d3a 100%); border-top-left-radius: 190px 220px; border-top-right-radius: 150px 200px; }

  .times-heading { position: absolute; left: 423px; top: 726px; margin: 0; font-weight: 900; font-size: 26px; letter-spacing: -1px; color: var(--red); }
  .day { position: absolute; color: var(--paper); }
  .day svg { position: absolute; left: -36px; top: 2px; }
  .day-name { display: block; font-weight: 400; font-size: 17px; letter-spacing: .8px; line-height: 24px; }
  .day-detail { display: block; font-weight: 800; font-size: 17px; letter-spacing: .4px; line-height: 24px; }
  .day-fri { left: 460px; top: 786px; }
  .day-sat { left: 633px; top: 786px; }
  .day-sun { left: 460px; top: 888px; }
  .sunday-time { position: absolute; left: 596px; top: 893px; width: 161px; height: 39px; background: var(--paper); color: var(--black); font-weight: 800; font-size: 20px; display: flex; align-items: center; justify-content: center; }
  .service-name { position: absolute; left: 423px; margin: 0; font-weight: 800; font-size: 19px; letter-spacing: 1px; color: var(--paper); white-space: nowrap; }
  .service-renewal { top: 973px; }
  .service-time { position: absolute; left: 423px; top: 1005px; margin: 0; font-weight: 800; font-size: 21px; color: var(--red); }
  .service-twofold { top: 1037px; font-size: 17px; }

  .guest { position: absolute; left: 420px; top: 1118px; margin: 0; color: var(--grey-text); }
  .guest-label { display: block; font-weight: 400; font-size: 14px; letter-spacing: .6px; line-height: 18px; }
  .guest-name { display: block; font-weight: 800; font-size: 14px; letter-spacing: .8px; line-height: 18px; color: var(--ink); }
  .guest-role { display: block; font-weight: 400; font-size: 12px; letter-spacing: .4px; line-height: 18px; }
</style>
</head>
<body>
<main class="poster">
  <div class="brand">
    <div class="brand-mark"></div>
    <div class="brand-name">Grace Tabernacle</div>
  </div>

  <h1 class="title">
    <span class="title-line-1">SUMMIT</span>
    <span class="title-line-2">GATHERING</span>
    <span class="title-year">2021</span>
  </h1>

  <div class="hosts-photo">
    <div class="hosts-photo-fill" role="img" aria-label="Photo of the host pastors, a smiling couple, against purple stage lights"></div>
  </div>

  <section class="info-band">
    <svg width="800" height="136" viewBox="0 0 800 136" aria-hidden="true">
      <path d="M0 0 H434 C414 4 410 20 400 36 C392 50 380 56 360 56 H0 Z" fill="var(--black)"/>
    </svg>
    <h2 class="venue-heading">THE LOCATION OF THE EVENT IS:</h2>
    <p class="venue-address">Seattle Harborgate Lodge. 4817 North<br>92nd Avenue Seattle, WA 98134.</p>
    <div class="band-divider"></div>
    <p class="hosts-label">HOSTS OF THE CONFERENCE</p>
    <p class="hosts-names">GRACE TABERNACLE-PASTORS<br>RON N MOLLY</p>
  </section>

  <section class="schedule"></section>
  <div class="guest-photo" role="img" aria-label="Portrait of the guest minister in a houndstooth blazer"></div>

  <h2 class="times-heading">CONFERENCE TIMES.</h2>

  <div class="day day-fri">
    <svg width="18" height="18" viewBox="0 0 18 18" aria-hidden="true"><rect x="1.5" y="3" width="14" height="13" rx="1.5" fill="none" stroke="#fff" stroke-width="1.3"/><line x1="1.5" y1="7" x2="15.5" y2="7" stroke="#fff" stroke-width="1.3"/><line x1="5" y1="1" x2="5" y2="4.5" stroke="#fff" stroke-width="1.3"/><line x1="12" y1="1" x2="12" y2="4.5" stroke="#fff" stroke-width="1.3"/><circle cx="13" cy="13" r="3" fill="#151515" stroke="#fff" stroke-width="1.2"/></svg>
    <span class="day-name">FRIDAY</span>
    <span class="day-detail">August 20th</span>
    <span class="day-detail">6pm-8:30pm</span>
  </div>
  <div class="day day-sat">
    <svg width="18" height="18" viewBox="0 0 18 18" aria-hidden="true"><rect x="1.5" y="3" width="14" height="13" rx="1.5" fill="none" stroke="#fff" stroke-width="1.3"/><line x1="1.5" y1="7" x2="15.5" y2="7" stroke="#fff" stroke-width="1.3"/><line x1="5" y1="1" x2="5" y2="4.5" stroke="#fff" stroke-width="1.3"/><line x1="12" y1="1" x2="12" y2="4.5" stroke="#fff" stroke-width="1.3"/><circle cx="13" cy="13" r="3" fill="#151515" stroke="#fff" stroke-width="1.2"/></svg>
    <span class="day-name">SATURDAY</span>
    <span class="day-detail">August 21st</span>
    <span class="day-detail">6pm-8:30pm</span>
  </div>
  <div class="day day-sun">
    <svg width="18" height="18" viewBox="0 0 18 18" aria-hidden="true"><rect x="1.5" y="3" width="14" height="13" rx="1.5" fill="none" stroke="#fff" stroke-width="1.3"/><line x1="1.5" y1="7" x2="15.5" y2="7" stroke="#fff" stroke-width="1.3"/><line x1="5" y1="1" x2="5" y2="4.5" stroke="#fff" stroke-width="1.3"/><line x1="12" y1="1" x2="12" y2="4.5" stroke="#fff" stroke-width="1.3"/><circle cx="13" cy="13" r="3" fill="#151515" stroke="#fff" stroke-width="1.2"/></svg>
    <span class="day-name">SUNDAY</span>
    <span class="day-detail">August 22nd</span>
  </div>
  <div class="sunday-time">10am-1pm</div>

  <p class="service-name service-renewal">CHURCH RENEWAL SERVICE</p>
  <p class="service-time">5pm-7:30pm</p>
  <p class="service-name service-twofold">TWOFOLD BLESSING SERVICE</p>

  <p class="guest">
    <span class="guest-label">GUEST MINISTER</span>
    <span class="guest-name">BISHOP LORNA KIPROTICH</span>
    <span class="guest-role">(Cedar Ridge Evangelist)</span>
  </p>
</main>
</body>
</html>
```